Landing Page IT Security Vendor

We need a landing page that uses our colour scheme (www.veldonguard.com). We created a draft (see attached). We do not need standard stock template design pages. Please only apply if you can design pages from scratch and try to be as close as possible to our draft. It is ok to also purchase commecrial stock pictures

Coding

Coded - Design and coding required

Number of Pages Required

1 page

```html
<!DOCTYPE html>
<html lang="en">
<head>
<meta charset="utf-8">
<title>Veldon Guard – Security Awareness Training</title>
<link href="https://fonts.googleapis.com/css2?family=Titillium+Web:wght@300;400;600;700&display=swap" rel="stylesheet">
<style>
:root{
  --teal:#1bb3bd;
  --teal-dark:#138f97;
  --orange:#f5a524;
  --ink:#333;
  --muted:#666;
  --light:#f1f1f1;
  --white:#fff;
}
*{box-sizing:border-box;margin:0;padding:0}
html,body{width:692px;height:1200px;overflow:hidden}
body{position:relative;font-family:"Titillium Web",Arial,sans-serif;color:var(--ink);background:var(--light)}
.abs{position:absolute}

/* top bar */
.topbar{left:0;top:0;width:692px;height:29px;background:var(--teal);color:var(--white)}
.award{top:5px;display:flex;align-items:center;gap:6px;font-size:5.4px;line-height:1.3;white-space:nowrap}
.award svg{flex:none}
.nav-home{left:535px;top:6px;width:57px;height:17px;border:1px solid var(--white);border-radius:9px;font-size:7.5px;display:flex;align-items:center;justify-content:center}
.nav-solution{left:608px;top:9px;font-size:7.5px}

/* hero */
.hero{left:0;top:29px;width:692px;height:340px;background:linear-gradient(120deg,#4b5a3c 0%,#6f7e63 30%,#8a8f8a 55%,#a9a39b 75%,#cfcfcf 100%)}
.hero-text{left:0;width:692px;text-align:center;color:var(--white)}
.hero-kicker{top:131px;font-size:14px;font-weight:300}
.hero-title{top:168px;font-size:24px;font-weight:700;line-height:31px}
.btn-demo{left:298px;top:285px;width:96px;height:26px;border-radius:13px;background:var(--teal);color:var(--white);font-size:6.5px;font-weight:700;display:flex;align-items:center;justify-content:center}
.scroll-cue{left:336px;top:356px;width:26px;height:26px;border-radius:50%;background:var(--teal)}

/* help section */
.section-title{left:0;top:395px;width:692px;text-align:center;font-size:16.5px;font-weight:600}
.card{top:433px;width:182px;height:260px;background:var(--white);border-top:1px solid var(--teal)}
.card-image{height:106px}
.card-body{padding:6px 12px 0}
.card h3{color:var(--orange);font-size:9.5px;line-height:12.5px;font-weight:700;text-transform:uppercase;white-space:nowrap}
.card .lead{margin-top:3px;font-size:7.6px;line-height:10.5px;font-weight:700;color:#111;white-space:nowrap}
.card .copy{margin-top:4px;font-size:6.1px;line-height:10.3px;color:var(--muted);white-space:nowrap}
.card .more{margin-top:10px;font-size:7.6px;font-weight:700;color:var(--teal)}

/* mssp band */
.mssp{left:0;top:718px;width:692px;height:43px;background:var(--teal);color:var(--white);display:flex;align-items:center;justify-content:center;font-size:9.5px;font-weight:700}
.mssp a{color:#0c2a33;margin-left:5px;text-decoration:underline;font-weight:700}

/* trust */
.trust-left{left:0;top:761px;width:355px;height:223px;background:var(--light)}
.trust-right{left:355px;top:761px;width:337px;height:223px;background:var(--white)}
.trust-title{left:43px;top:796px;font-size:16px;line-height:20.5px;color:var(--teal);font-weight:400}
.trust-copy{left:43px;top:845px;width:290px;font-size:7.6px;line-height:11px;color:#444}
.trust-copy p{margin-bottom:11px}
.btn-contact{left:71px;top:944px;width:213px;height:21px;border-radius:11px;background:var(--teal);color:var(--white);font-size:7.5px;display:flex;align-items:center;justify-content:center}
.client{display:flex;align-items:center;gap:4px;font-size:9.5px;font-weight:700;color:#3a3a3a;white-space:nowrap}
.client i{display:block;width:9px;height:9px;background:var(--teal)}

/* footer */
.footer{left:0;top:984px;width:692px;height:193px;background:var(--teal-dark)}
.foot-col{top:1004px;font-size:7.4px;line-height:11px;color:var(--white)}
.foot-col h4{font-size:10px;font-weight:700;padding-bottom:3px;margin-bottom:12px;position:relative;color:var(--white)}
.foot-col h4::after{content:"";position:absolute;left:0;bottom:0;width:40px;height:1.5px;background:#5fd3da}
.info li{list-style:none;padding-left:8px;position:relative;line-height:12.2px}
.info li::before{content:"";position:absolute;left:0;top:4px;border-left:3.5px solid #9be6ea;border-top:2.5px solid transparent;border-bottom:2.5px solid transparent}
.socials{display:flex;gap:8px;margin-top:9px}
.socials span{width:17px;height:17px;border:1.2px solid var(--white);border-radius:50%}
.lang-select{width:78px;height:13px;border:1px solid var(--white);display:flex;align-items:center;font-size:5px}
.lang-select b{width:12px;height:100%;border-right:1px solid var(--white);display:flex;align-items:center;justify-content:center;font-weight:400}
.search{width:86px;height:12px;display:flex}
.search span{flex:1;border:1px solid var(--white);font-size:5.5px;padding-left:6px;line-height:10px}
.search b{width:12px;background:var(--white)}
.bottom-bar{left:0;top:1177px;width:692px;height:23px;background:var(--teal);color:#124;font-size:4.5px;display:flex;align-items:center;justify-content:center}
.bottom-bar strong{color:var(--white);margin-left:2px}
</style>
</head>
<body>

<header class="abs topbar">
  <div class="abs award" style="left:50px">
    <svg width="14" height="14" viewBox="0 0 14 14" fill="none" stroke="#fff" stroke-width="1"><path d="M4 2h6v4a3 3 0 0 1-6 0z"/><path d="M7 9v2M4.5 12h5"/><path d="M4 3H2v1a2 2 0 0 0 2 2M10 3h2v1a2 2 0 0 1-2 2"/></svg>
    <span>in 2020 VELDON won the Secure Futures<br>Award for Best "Anti Phishing"</span>
  </div>
  <div class="abs award" style="left:209px">
    <svg width="15" height="14" viewBox="0 0 15 14" fill="none" stroke="#fff" stroke-width="1"><path d="M2 4l3 3 2.5-5 2.5 5 3-3-1 7H3z"/><path d="M3 12.5h9"/></svg>
    <span>in 2020 VELDON won the Secure Futures<br>Award for Best "Security Education Platform"</span>
  </div>
  <div class="abs award" style="left:368px">
    <svg width="14" height="14" viewBox="0 0 14 14" fill="none" stroke="#fff" stroke-width="1"><circle cx="7" cy="6" r="4"/><path d="M7 4l.7 1.4 1.5.2-1.1 1 .3 1.5L7 7.4l-1.4.7.3-1.5-1.1-1 1.5-.2z"/><path d="M4.5 9l-1.5 4 2-1 1 1.5M9.5 9l1.5 4-2-1-1 1.5"/></svg>
    <span>2020 Gold Winner "Awareness Education<br>Honours" in the Digital Defense Review</span>
  </div>
  <div class="abs nav-home">HOME</div>
  <div class="abs nav-solution">Solution &nbsp;⌄</div>
</header>

<section class="abs hero" role="img" aria-label="Photo of two excited children pointing at a laptop screen"></section>
<div class="abs hero-text hero-kicker">CYBER SECURITY STARTS WITH PEOPLE</div>
<h1 class="abs hero-text hero-title">TRAIN YOUR STAFF WITH VELDON<br>AND IMPROVE CYBER SECURITY<br>AWARENESS</h1>
<div class="abs btn-demo">REQUEST A DEMO</div>
<div class="abs scroll-cue">
  <svg width="26" height="26" viewBox="0 0 26 26"><path d="M7.5 10.5L13 16l5.5-5.5" fill="none" stroke="#fff" stroke-width="1.6" stroke-linecap="round"/></svg>
</div>

<h2 class="abs section-title">How Can we Help?</h2>

<article class="abs card" style="left:43px">
  <div class="card-image" role="img" aria-label="Photo of a person working at a desktop computer" style="background:linear-gradient(135deg,#5c6167,#c9c6c0 55%,#8a7d70)"></div>
  <div class="card-body">
    <h3>Import our training courses<br>in your LMS</h3>
    <p class="lead">Buy out of the box custon tailored<br>security courses you can import in your<br>Elearning(SCORM)</p>
    <p class="copy">Lorem ipsum dolor sit amet, consectetur adipiscing<br>elit, sed do eiusmod tempor incididunt ut labore et<br>dolore magna aliqua. Quis ipsum suspendisse<br>ultrices gravida. Risus commodo viverra maecenas</p>
    <p class="more">&gt;&gt;&gt; EXPLORE OUR TRAINING</p>
  </div>
</article>

<article class="abs card" style="left:255px">
  <div class="card-image" role="img" aria-label="Photo of a laptop showing code on a desk" style="background:linear-gradient(180deg,#d9d9d9,#9a9a9a 55%,#3b3b3b)"></div>
  <div class="card-body">
    <h3>Let us develop a security<br>awareness program</h3>
    <p class="lead">VELDON Security will assist you in improving<br>security awareness with money back<br>guarantee!</p>
    <p class="copy">Lorem ipsum dolor sit amet, consectetur adipiscing<br>elit, sed do eiusmod tempor incididunt ut labore et<br>dolore magna aliqua. Quis ipsum suspendisse<br>ultrices gravida. Risus commodo viverra maecenas</p>
    <p class="more">&gt;&gt;&gt; EXPLORE OUR TRAINING</p>
  </div>
</article>

<article class="abs card" style="left:467px">
  <div class="card-image" role="img" aria-label="Photo of a keyboard seen through a magnifying glass" style="background:linear-gradient(135deg,#2d4a7a,#7f9cc8 50%,#1e2d4a)"></div>
  <div class="card-body">
    <h3>Install the Veldon software<br>on-promise or get access<br>to the SaaS version</h3>
    <p class="lead">You want to run the camaign yourself?<br>Choose you prefers setup type and get<br>started in 24h!</p>
    <p class="copy">Lorem ipsum dolor sit amet, consectetur adipiscing<br>elit, sed do eiusmod tempor incididunt ut labore et<br>dolore magna aliqua. Quis ipsum suspendisse</p>
    <p class="more">&gt;&gt;&gt; EXPLORE OUR TRAINING</p>
  </div>
</article>

<div class="abs mssp">VELDON is also available for MSSP - <a>Learn More</a></div>

<section class="abs trust-left"></section>
<section class="abs trust-right"></section>
<h2 class="abs trust-title">Already over 12.000.000 Employees<br>WorldWide trust and use VELDON.</h2>
<div class="abs trust-copy">
  <p>Veldon Security in a name you can trust! Becausewe have won contless awards since 2015 and help well-known brands around the world.</p>
  <p>You know you're getting a quality solution with u.</p>
  <p>Our services can be customized to fit your need and company size.<br>Talk to our team today to learn more.</p>
</div>
<div class="abs btn-contact">GET IN CONTACT WITH THE VELDON TEAM NOW!</div>

<div class="abs client" style="left:411px;top:799px"><i></i>NORVALE</div>
<div class="abs client" style="left:480px;top:799px"><i></i>OSTRAIL</div>
<div class="abs client" style="left:569px;top:799px"><i></i>Hausmeta</div>
<div class="abs client" style="left:411px;top:853px"><i></i>KERNTEK</div>
<div class="abs client" style="left:520px;top:853px"><i></i>ALPWING</div>
<div class="abs client" style="left:411px;top:901px"><i></i>MAHLBERG</div>
<div class="abs client" style="left:534px;top:901px"><i></i>RENNWERK DATA</div>
<div class="abs client" style="left:411px;top:946px"><i></i>CHEMIVO</div>
<div class="abs client" style="left:534px;top:946px"><i></i>Stadtpflege Nord</div>

<footer class="abs footer"></footer>
<div class="abs foot-col" style="left:43px">
  <h4>CONTACT US</h4>
  <p>Address: Europe<br>Veldon Guard AG<br>Seeweg 18 | 6301 Lakeside | Switzerland</p>
  <p style="margin-top:11px">Address: North America<br>Veldon Guard USA<br>4210 Harbor Way<br>Suite 200<br>Denver, CO 80202</p>
</div>
<div class="abs foot-col" style="left:203px">
  <h4>CONNECT WITH US</h4>
  <p style="line-height:13px">Phone Global: +41 44 000 12 34<br>Phone USA: +1-555-010-2200<br>Phone USA Support: +1-555-010-2211<br>Phone France: +33 600 000 111<br>Phone UK: +44 (0) 7000 000123</p>
  <div class="socials"><span></span><span></span><span></span><span></span></div>
</div>
<div class="abs foot-col" style="left:360px">
  <h4>INFORMATION</h4>
  <ul class="info">
    <li>Home</li><li>Solution</li><li>Pricing</li><li>Resources</li><li>About us</li><li>Support Wiki</li><li>Contact</li><li>Download VELDON</li><li>Demo request</li>
  </ul>
</div>
<div class="abs foot-col" style="left:524px">
  <h4>LANGUAGE</h4>
  <div class="lang-select"><b>⌄</b><span style="margin-left:14px">English</span></div>
  <h4 style="margin-top:26px">SEARCH</h4>
  <div class="search"><span>search</span><b></b></div>
</div>
<div class="abs bottom-bar">All Rights Reserved 2020 <strong>VELDON</strong></div>

</body>
</html>
```